Kleine-Entdecker-Tag Flyer
Zielgruppe
Eltern, die ihre Kinder in ihrer Entwicklung fördern möchten.
Aufgabenstellung
Wir organisieren eine Messe mit dem Thema "Kleine Entdecker Tag". Bei der Messe geht es nicht um das Lernen über Bücher (alleine) oder das Schulische, sondern die Messe soll für Eltern sein, die ihre Kinder fördern möchten durch die Behebung von Lernblockaden, Förderung der Konzentration, Kreativität, spielerisches Lernen etc. Es geht um Kinder ab ca. 4 Jahren.
Als Aussteller werden verschiedene Themen angesprochen: Kinesiologie, Logopädie, Privatschulen mit speziellem Angenbot, Schachunterricht, spielerisches Lernangebot, Kindermalen etc. , alles was darauf zielt, Kreativität und Lernen bei Kindern zu fördern.
Wir brauchen daher einen Flyer, der die Eltern anspricht. Die Messe findet am Sonntag, 9.11.2012 statt. Beginn 11 Uhr, Ende 18.00 Uhr. Ort: Lindenhalle - Ahornsaal, Felsbergweg 7, 8047 Zürich.
Das Logo wird attached. Das Format ist frei wählbar.

```html
<!DOCTYPE html>
<html lang="de">
<head>
<meta charset="utf-8">
<title>Kleine Entdecker Tag – Messe Zürich</title>
<link href="https://fonts.googleapis.com/css2?family=Fredoka:wght@500;600&family=Open+Sans:wght@400;600;700&family=Space+Mono:wght@700&display=swap" rel="stylesheet">
<style>
  :root {
    --orange: #f39a1e;
    --orange-dark: #e98a10;
    --purple: #8e1a7d;
    --blue: #1e9ad6;
    --grey: #555555;
    --teal: #109a94;
    --white: #ffffff;
    --board: #4d4d4d;
    --photo-light: #e9d8c8;
    --photo-mid: #e79a4a;
  }
  * { margin: 0; padding: 0; box-sizing: border-box; }
  html, body { width: 1200px; height: 910px; overflow: hidden; background: var(--board); }
  body { position: relative; font-family: "Open Sans", Arial, sans-serif; }

  .poster {
    position: absolute; left: 25px; top: 45px; width: 552px; height: 775px;
    background: var(--white); overflow: hidden;
    box-shadow: 4px 4px 8px rgba(0,0,0,.45);
  }
  .poster__head { position: absolute; left: 0; top: 0; width: 100%; height: 174px; background: var(--orange); }
  .poster__title {
    position: absolute; left: 28px; top: 34px;
    font-family: "Fredoka", sans-serif; font-weight: 600; font-size: 56px; line-height: 1;
    color: var(--purple); letter-spacing: -0.5px;
  }
  .poster__subtitle {
    position: absolute; left: 30px; top: 102px;
    font-family: "Fredoka", sans-serif; font-weight: 600; font-size: 34px;
    color: var(--purple); letter-spacing: 1px;
  }
  .poster__info {
    position: absolute; left: 0; top: 174px; width: 100%; height: 100px; background: var(--purple);
    color: var(--white); padding: 12px 0 0 28px;
  }
  .poster__time { font-weight: 700; font-size: 20px; line-height: 1.3; }
  .poster__venue { font-size: 17px; line-height: 1.4; }
  .poster__date {
    position: absolute; left: 26px; top: 292px;
    font-weight: 700; font-size: 50px; line-height: 1.3; color: var(--purple);
  }
  .poster__photo {
    position: absolute; left: 300px; top: 168px; width: 252px; height: 525px;
    background: linear-gradient(180deg, var(--photo-light) 0%, #d9c4b0 35%, var(--photo-mid) 70%, #d98532 100%);
  }
  .brand {
    position: absolute; display: flex; align-items: center; gap: 8px;
    font-family: "Open Sans", sans-serif; font-weight: 600; color: var(--teal);
  }
  .brand__dot { width: 14px; height: 14px; border-radius: 50%; background: var(--teal); flex: none; }
  .poster__brand { left: 30px; top: 548px; font-size: 20px; }
  .poster__url { position: absolute; left: 60px; top: 578px; font-size: 10px; color: var(--grey); }
  .poster__claim {
    position: absolute; left: 0; top: 610px; width: 300px; height: 82px; background: var(--purple);
    color: var(--white); font-weight: 700; font-size: 14.5px; line-height: 1.35; padding: 14px 0 0 28px;
  }
  .poster__foot {
    position: absolute; left: 0; top: 692px; width: 100%; height: 83px; background: var(--orange);
    color: var(--purple); font-weight: 700; font-size: 14.5px; line-height: 1.75; padding: 18px 0 0 30px;
  }

  .pill {
    position: absolute; z-index: 2; width: 170px; height: 60px; border-radius: 30px;
    color: var(--white); font-weight: 700; text-align: center;
    display: flex; align-items: center; justify-content: center; line-height: 1.2;
    transform: rotate(-24deg);
  }
  .pill--blue { background: var(--blue); }
  .pill--grey { background: var(--grey); }
  .pill--teal { background: var(--teal); }
  .pill--orange { background: var(--orange); }
  .pill--purple { background: var(--purple); }
  .poster .pill { font-size: 15px; padding-right: 12px; }
  .poster .pill--blue { left: 400px; top: 488px; }
  .poster .pill--grey { left: 400px; top: 562px; }
  .poster .pill--teal { left: 400px; top: 632px; }

  .card-front {
    position: absolute; left: 612px; top: 172px; width: 466px; height: 230px;
    background: var(--white); overflow: hidden; box-shadow: 4px 4px 8px rgba(0,0,0,.45);
  }
  .card-front__stripe { position: absolute; left: 0; top: 0; width: 100%; height: 26px; background: var(--orange); }
  .card-front__brand { left: 22px; top: 88px; font-size: 15px; }
  .card-front__url { position: absolute; left: 86px; top: 116px; font-size: 8px; color: var(--grey); }
  .card-front__band { position: absolute; left: 0; top: 146px; width: 100%; height: 84px; background: var(--purple); }
  .card-front__title {
    position: absolute; left: 22px; top: 140px;
    font-family: "Space Mono", monospace; font-weight: 700; font-size: 33px; color: var(--white);
  }
  .card-front__name {
    position: absolute; left: 16px; top: 186px;
    font-family: "Space Mono", monospace; font-weight: 700; font-size: 21px; color: var(--white);
  }
  .card-front__name .t { color: var(--teal); }
  .card-front__name .o { color: var(--orange); }
  .card-front__photo {
    position: absolute; left: 318px; top: 28px; width: 118px; height: 200px;
    background: linear-gradient(180deg, var(--photo-light) 0%, #cfc0b2 40%, var(--photo-mid) 75%, #b98c5c 100%);
  }

  .card-back {
    position: absolute; left: 640px; top: 418px; width: 470px; height: 232px;
    background: var(--white); overflow: hidden; transform: rotate(-8deg); transform-origin: center;
    box-shadow: 4px 4px 8px rgba(0,0,0,.45);
  }
  .card-back__top { position: absolute; left: 0; top: 0; width: 100%; height: 118px; background: var(--orange); }
  .card-back__info { position: absolute; left: 26px; top: 22px; color: var(--white); }
  .card-back__time { font-weight: 700; font-size: 17px; line-height: 1.6; }
  .card-back__venue { font-size: 13.5px; line-height: 1.45; }
  .card-back__claim { position: absolute; left: 26px; top: 124px; font-size: 8.5px; line-height: 1.35; color: var(--grey); }
  .card-back__date {
    position: absolute; left: 48px; top: 164px;
    font-family: "Space Mono", monospace; font-weight: 700; font-size: 34px; color: var(--purple);
  }
  .card-back .pill { width: 104px; height: 42px; font-size: 10.5px; transform: rotate(-38deg); }
  .card-back .pill--teal { left: 352px; top: 14px; }
  .card-back .pill--orange { left: 364px; top: 64px; }
  .card-back .pill--purple { left: 372px; top: 114px; }
</style>
</head>
<body>
  <section class="poster">
    <div class="poster__head">
      <h1 class="poster__title">Kleine Entdecker</h1>
      <p class="poster__subtitle">MESSE ZÜRICH</p>
    </div>
    <div class="poster__info">
      <p class="poster__time">11 Uhr - 18.00 Uhr.</p>
      <p class="poster__venue">Lindenhalle-Ahornsaal,<br>Felsbergweg 7, 8047 Zürich.</p>
    </div>
    <div class="poster__photo" role="img" aria-label="Foto: Kind sitzt mit Tablet auf einem Bücherstapel"></div>
    <p class="poster__date">Sonntag<br>9.11.2012</p>
    <div class="brand poster__brand"><span class="brand__dot"></span>Kleine Entdecker Tag</div>
    <p class="poster__url">www.kleine-entdecker-tag.ch</p>
    <p class="poster__claim">... damit Kindern ihre aktuellen<br>und zukünftigen Herausforderungen<br>spielend meistern!</p>
    <div class="poster__foot">
      www.kleine-entdecker-tag.de<br>
      Veranstalter: Kleine Entdecker GmbH, Am Mühlebach 12, 8834 Seeberg
    </div>
    <div class="pill pill--blue">Konzentration<br>fördern</div>
    <div class="pill pill--grey">Lernen<br>entfalten</div>
    <div class="pill pill--teal">Begabungen<br>erkennen</div>
  </section>

  <section class="card-front">
    <div class="card-front__stripe"></div>
    <div class="brand card-front__brand"><span class="brand__dot"></span>Kleine Entdecker Tag</div>
    <p class="card-front__url">www.kleine-entdecker-tag.ch</p>
    <div class="card-front__band"></div>
    <div class="card-front__photo" role="img" aria-label="Foto: Kind mit Tablet auf Bücherstapel"></div>
    <p class="card-front__title">MESSE ZÜRICH</p>
    <p class="card-front__name">"<span class="t">Kleine</span>&amp;<span class="o">Entdecker</span>"</p>
  </section>

  <section class="card-back">
    <div class="card-back__top"></div>
    <div class="card-back__info">
      <p class="card-back__time">11 Uhr - 18.00 Uhr</p>
      <p class="card-back__venue">Lindenhalle-Ahornsaal,<br>Felsbergweg 7, 8047 Zürich.</p>
    </div>
    <p class="card-back__claim">... damit Kindern ihre aktuellen und zukünftigen Herausforderungen<br>spielend meistern!</p>
    <p class="card-back__date">Sonntag, 9.11.2012</p>
    <div class="pill pill--teal">Konzentration<br>fördern</div>
    <div class="pill pill--orange">Lernen<br>entfalten</div>
    <div class="pill pill--purple">Begabungen<br>erkennen</div>
  </section>
</body>
</html>
```